Cradlecraft by Lorna Business Card Design

i am starting a new business as a reborn artist (that is painting dolls to make them look like real live babies)

i eventually want to sell the dolls that i make and have classed in reborning. but at the moment i just want to get my name out there.

I do not currently have images of the dolls so cannot have an image in the design.

Non compulsory thoughts: i like the look of old wood, white and baby pink,even hot pink, and lace, denim. i had in mind something like a tiny baby in a old cradle or something, a old drawer, box, something different or unusual, it has to be a girl baby. i am also open to other thoughts on the matter. i would like plain writing not all swirly
Updates

Sorry to change but would like it to read country cradlecraft by lorna.

Industry/Entity Type

Painting

Contact Information for Business Card

Cradlecraft by Lorna
Gentle Keepsakes for Loving Arms
Reborn Artist Lorna Whitby
0431 756 842
marlo.t@quillbox.com

```html
<!DOCTYPE html>
<html lang="en">
<head>
<meta charset="utf-8">
<title>Country Cradlecraft by Lorna – Business Card</title>
<link href="https://fonts.googleapis.com/css2?family=Great+Vibes&family=Questrial&display=swap" rel="stylesheet">
<style>
  :root {
    --page-bg: #eceeee;
    --card-bg: #ffffff;
    --rose: #c9446a;
    --band-pink: #f2a1b3;
    --check-pink: #f4b6c4;
    --check-light: #fbdde4;
    --ink: #333333;
    --white: #ffffff;
  }
  * { margin: 0; padding: 0; box-sizing: border-box; }
  html, body {
    width: 1200px;
    height: 856px;
    overflow: hidden;
    background: var(--page-bg);
  }
  .business-card {
    position: absolute;
    left: 50px;
    top: 90px;
    width: 1100px;
    height: 677px;
    background: var(--card-bg);
    border-radius: 40px;
    overflow: hidden;
  }
  .gingham-field {
    position: absolute;
    left: 0;
    top: 270px;
    width: 100%;
    height: 407px;
    background:
      linear-gradient(to bottom, rgba(255,255,255,1) 0%, rgba(255,255,255,0.35) 30%, rgba(255,255,255,0) 60%),
      linear-gradient(135deg, var(--check-light) 0%, var(--check-pink) 45%, var(--check-light) 70%, var(--check-pink) 100%);
  }
  .doll-photo {
    position: absolute;
    left: 638px;
    top: 37px;
    width: 462px;
    height: 402px;
    background: radial-gradient(ellipse at 50% 50%, #f3c3cd 0%, #f7dbe1 38%, #fdf3f5 62%, rgba(255,255,255,0) 78%);
  }
  .brand-name {
    position: absolute;
    left: 0;
    top: 50px;
    width: 1100px;
    padding-right: 80px;
    text-align: center;
    font-family: "Questrial", sans-serif;
    font-weight: 400;
    font-size: 40px;
    color: var(--rose);
    line-height: 1.2;
  }
  .role {
    position: absolute;
    left: 140px;
    top: 190px;
    font-family: "Questrial", sans-serif;
    font-size: 30px;
    color: var(--ink);
  }
  .artist-name {
    position: absolute;
    left: 86px;
    top: 232px;
    font-family: "Great Vibes", cursive;
    font-size: 56px;
    word-spacing: 10px;
    color: var(--rose);
    line-height: 1.2;
  }
  .contact {
    position: absolute;
    left: 92px;
    display: flex;
    align-items: center;
    gap: 16px;
    font-family: "Questrial", sans-serif;
    font-size: 31px;
    color: var(--ink);
  }
  .contact svg { width: 30px; height: 30px; flex: none; }
  .contact--phone { top: 314px; }
  .contact--email { top: 366px; }
  .tagline-band {
    position: absolute;
    left: 0;
    top: 469px;
    width: 100%;
    height: 71px;
    background: var(--band-pink);
    display: flex;
    align-items: center;
    justify-content: center;
    font-family: "Great Vibes", cursive;
    font-size: 44px;
    color: var(--white);
  }
</style>
</head>
<body>
  <div class="business-card">
    <div class="gingham-field" role="img" aria-label="Soft pink gingham check pattern"></div>
    <div class="doll-photo" role="img" aria-label="Photo of a reborn baby girl doll in a pink dress and lace bonnet"></div>

    <h1 class="brand-name">Country Cradlecraft by Lorna</h1>

    <p class="role">Reborn Artist</p>
    <p class="artist-name">Lorna Whitby</p>

    <p class="contact contact--phone">
      <svg viewBox="0 0 24 24" aria-hidden="true">
        <rect x="6" y="4" width="12" height="17" rx="1.5" fill="none" stroke="#333" stroke-width="1.8"/>
        <line x1="6" y1="17" x2="18" y2="17" stroke="#333" stroke-width="1.5"/>
        <circle cx="12" cy="19" r="0.9" fill="#333"/>
      </svg>
      0431 756 842
    </p>
    <p class="contact contact--email">
      <svg viewBox="0 0 24 24" aria-hidden="true">
        <rect x="2.5" y="6" width="19" height="12" fill="none" stroke="#333" stroke-width="1.8"/>
        <polyline points="2.5,6 12,13 21.5,6" fill="none" stroke="#333" stroke-width="1.6"/>
        <polyline points="2.5,18 9.5,11.5" fill="none" stroke="#333" stroke-width="1.4"/>
        <polyline points="21.5,18 14.5,11.5" fill="none" stroke="#333" stroke-width="1.4"/>
      </svg>
      marlo.t@quillbox.com
    </p>

    <div class="tagline-band">Gentle Keepsakes for Loving Arms</div>
  </div>
</body>
</html>
```